New look and feel for investment website

Hi

Our website needs a crisp and professional look and feel applying to it. Here’s the address: http://www.brightplinth.co.uk. Since posting the brief yesterday (Tuesday, 16 August), we've reduced the amount of content on the home page, which should make life a little easier for you. We will come back later today, with some points of reference in terms of sites we like the look of. (See below)

17 August, 1.20pm GMT. OK, comments generally on the designs submitted so far. Please keep in mind that images of graphs, piles of coins, paper money and pretty females are not what is required. Better to think in terms of abstract imagery instead. Ratios? Circles? Relationships? Patterns? Not money,sex,graphs etc. Hope that helps.

For guidance on look and feel, please refer to these sites, which we like:

http://www.morvelle.co.uk/
http://www.qz.com/
https://www.harrowfieldtamsin.com
https://www.pirelconcerns.com
https://www.kvantule.com
Updates

Here's the Tall Beacons logo created in AI CS5.

Our market is professional financial advisers and relatively sophisticated private investors. The look and feel therefore should be slick and sophisticated - not 'lively' and lightweight, more like a banking site. Please read the brief again where we've added a list of websites that we really like the look of to get a better feel for what we're looking for. Thanks once again, we appreciate the work you're putting in.

It's essential that all the elements that are on the current home page be included on all new designs. 

We use a device in our e-mails which you may wish to incorporate in your design.

Target Market(s)

Professional financial advisers. People who know about investment and money.

Industry/Entity Type

Investment

Requirements
Should not have
• Graphs or people.

```html
<!DOCTYPE html>
<html lang="en">
<head>
<meta charset="utf-8">
<title>Tall Beacons – Home</title>
<link rel="stylesheet" href="https://fonts.googleapis.com/css2?family=Arvo:wght@700&family=Open+Sans:wght@400;600;700&display=swap">
<style>
  :root {
    --navy: #1e3a4f;
    --navy-dark: #16303f;
    --red: #d8394e;
    --teal: #1aa3c4;
    --teal-button: #17a0ba;
    --text: #3d4a54;
    --muted: #8a96a0;
    --panel-grey: #ebedee;
    --white: #ffffff;
  }
  * { box-sizing: border-box; margin: 0; padding: 0; }
  html, body { width: 884px; height: 1200px; overflow: hidden; background: var(--white); }
  body { position: relative; font-family: "Open Sans", Arial, sans-serif; color: var(--text); font-size: 9.5px; line-height: 13.5px; }

  .site-header { position: absolute; left: 0; top: 0; width: 884px; height: 201px; z-index: 2; }

  .brand { position: absolute; left: 146px; top: 28px; display: flex; align-items: center; gap: 8px; }
  .brand-square { width: 18px; height: 18px; background: var(--red); }
  .brand-name { font-family: "Open Sans", Arial, sans-serif; font-weight: 700; font-size: 16px; letter-spacing: 0.5px; color: var(--navy); }

  .utility-nav { position: absolute; right: 145px; top: 36px; font-size: 9px; color: var(--muted); }
  .utility-nav a { color: var(--muted); text-decoration: none; }
  .utility-nav a.highlight { color: var(--red); }
  .utility-nav .sep { margin: 0 5px; }

  .rule { position: absolute; left: 145px; width: 594px; height: 4px; background: var(--navy); }
  .rule.top { top: 70px; }
  .rule.bottom { top: 197px; }

  .headline { position: absolute; left: 154px; top: 95px; font-family: "Arvo", Georgia, serif; font-weight: 700; font-size: 18px; line-height: 23.5px; color: var(--navy-dark); white-space: nowrap; }

  .main-nav { position: absolute; left: 596px; top: 83px; list-style: none; }
  .main-nav li { position: relative; display: block; height: 9.9px; line-height: 9px; }
  .main-nav a { display: inline-block; background: var(--navy); color: var(--white); font-family: "Arvo", Georgia, serif; font-size: 6.8px; line-height: 9px; padding: 0 4px; text-decoration: none; white-space: nowrap; vertical-align: top; }
  .main-nav li.current a { background: var(--red); }
  .main-nav li.current::before { content: ""; position: absolute; left: -9px; top: 1.5px; border-left: 5px solid var(--navy); border-top: 3px solid transparent; border-bottom: 3px solid transparent; }

  .backdrop { position: absolute; left: 0; top: 201px; width: 884px; height: 780px; z-index: 0;
    background: linear-gradient(100deg, #f3b046 0%, #d8394e 18%, #9fb9c2 34%, #f4f4f4 50%, #c7dee0 64%, #d8394e 80%, #2c6685 100%); opacity: 0.85; }

  .content-card { position: absolute; left: 145px; top: 226px; width: 594px; height: 676px; background: var(--white); box-shadow: 0 0 0 1px rgba(0,0,0,0.06); z-index: 1; }

  .intro { position: absolute; left: 26px; top: 36px; width: 262px; }
  .section-title { font-weight: 600; font-size: 11px; color: var(--navy-dark); letter-spacing: 0.2px; padding-bottom: 8px; border-bottom: 1px solid var(--teal); margin-bottom: 12px; }
  .intro p { margin-bottom: 12px; }
  .intro h3 { font-size: 8.8px; font-weight: 700; color: var(--teal); margin-bottom: 6px; line-height: 13px; }
  .intro .section-title.second { margin-top: 26px; margin-bottom: 26px; }

  .stats { position: absolute; left: 365px; top: 36px; width: 200px; }
  .stats .section-title { margin-bottom: 14px; }
  .stat-list { list-style: none; }
  .stat { display: flex; justify-content: space-between; align-items: stretch; background: var(--panel-grey); min-height: 36px; margin-bottom: 6px; }
  .stat-label { padding: 6px 10px; font-size: 8.5px; line-height: 12px; display: flex; align-items: center; }
  .stat-value { flex: 0 0 43px; background: var(--red); color: var(--white); font-weight: 700; font-size: 8.5px; display: flex; align-items: center; justify-content: center; }
  .stat.note .stat-label { padding: 7px 10px; }
  .signup { display: block; margin-top: 8px; background: var(--teal-button); color: var(--white); text-align: center; font-family: "Arvo", Georgia, serif; font-size: 11px; line-height: 40px; text-decoration: none; letter-spacing: 0.3px; }

  .footer { position: absolute; left: 145px; top: 1026px; width: 594px; font-size: 8.3px; line-height: 12px; }
  .footer .questions { font-weight: 700; color: #8493a0; margin-bottom: 10px; }
  .footer .questions a { color: var(--teal); }
  .footer .legal { color: #a0abb4; }
</style>
</head>
<body>
  <header class="site-header">
    <div class="brand"><span class="brand-square"></span><span class="brand-name">TALL BEACONS</span></div>
    <nav class="utility-nav">
      <a href="#">Login</a><span class="sep">|</span><a class="highlight" href="#">Register for free</a><span class="sep">|</span><a href="#">Contact us</a><span class="sep">|</span><a href="#">Terms &amp; Conditions</a>
    </nav>
    <div class="rule top"></div>
    <h1 class="headline">A potential return of 23.57 % a year from<br>America’s biggest businesses with the<br>emphasis firmly on capital preservation.</h1>
    <ul class="main-nav">
      <li class="current"><a href="#">Home</a></li>
      <li><a href="#">Two Minute Guide</a></li>
      <li><a href="#">Current &amp; year to date performance</a></li>
      <li><a href="#">Watch list</a></li>
      <li><a href="#">Other key numbers</a></li>
      <li><a href="#">Back tested results</a></li>
      <li><a href="#">History of all trades</a></li>
      <li><a href="#">FAQs</a></li>
      <li><a href="#">About our analyses</a></li>
      <li><a href="#">About value investing</a></li>
      <li><a href="#">The Broadline 1000 and the Meridian 500 index</a></li>
    </ul>
    <div class="rule bottom"></div>
  </header>

  <div class="backdrop" role="img" aria-label="Abstract backdrop of overlapping translucent geometric shapes in red, orange, teal and navy"></div>

  <main class="content-card">
    <section class="intro">
      <h2 class="section-title">SOMETHING DIFFERENT...</h2>
      <p>You may well be thinking that Tall Beacons is just another one of those banal share recommendation sites sprinkled with the usual idiotic and patronising platitudes, gross exaggerations, silly get-rich-quick promises and all the other stuff and nonsense you associate with the black art of share-tipping...</p>
      <h2 class="section-title second">YOU COULDN’T BE FURTHER FROM THE TRUTH.</h2>
      <h3>No! No! No!</h3>
      <p>There’s no newsletter to read, books to study, dvds to watch or traders’ secrets to be revealed. No never-ending stream of recommendations. No webcasts. No effort or time to invest. No training. No research. No tedious market commentaries. And no financial discomfort for you whatsoever. (At least for the first six months that is!)</p>
      <h3>Undervalued and overlooked</h3>
      <p>Our program finds stocks that appear to be undervalued - i.e., where the price of a company’s share does not reflect the real worth of the business. We confine our search to 1,000 of the USA’s biggest companies; successful, robust, large cap businesses, which for one reason or another are either unpopular with investors or overlooked by them</p>
      <h3>We don’t get it right every time...</h3>
      <p>We do however, get it right 75.58 % of the time (the total of all our winning trades out of all our trades) and on that basis tracking our portfolio should produce an average return of 23.57 % a year for you</p>
      <h3>An average of five trades a year and never more than five holdings</h3>
      <p>We tested different numbers of holdings and capital allocation percentages. The best results came from a portfolio of no more than five holdings with the same amount of capital allocated to each holding. That’s it. You don’t have to do it that way, but it works for us.</p>
    </section>

    <aside class="stats">
      <h2 class="section-title">OUR STATS</h2>
      <ul class="stat-list">
        <li class="stat"><span class="stat-label">Average, annualised compound return over to</span><span class="stat-value">23.57 %</span></li>
        <li class="stat"><span class="stat-label">So far this year, the portfolio’s return is</span><span class="stat-value">13.49 %</span></li>
        <li class="stat"><span class="stat-label">Worst ever annual loss:</span><span class="stat-value">-1.48 %</span></li>
        <li class="stat"><span class="stat-label">Best ever annual gain:</span><span class="stat-value">69.77 %</span></li>
        <li class="stat"><span class="stat-label">Average return per trade including losing trades:</span><span class="stat-value">24.44 %</span></li>
        <li class="stat"><span class="stat-label">Maximum number of winning/ losing trades in a row:</span><span class="stat-value">11/4</span></li>
        <li class="stat"><span class="stat-label">Average number of days a stock stays in the portfolio:</span><span class="stat-value">287</span></li>
        <li class="stat note"><span class="stat-label">An average of five trades a year and never more than five holdings at any one time</span></li>
        <li class="stat note"><span class="stat-label">86 trades in total, of which 65 were profitable - a success rate of 75.58 %</span></li>
      </ul>
      <a class="signup" href="#">SIGN UP NOW FOR FREE</a>
    </aside>
  </main>

  <footer class="footer">
    <p class="questions">If you have any questions, please e-mail <a href="#">info@brightplinth.co.uk</a>. Although we’re very willing to answer queries about the way we pick stocks, please do keep in mind that as we’re giving this service away free of charge initially, we’re not inclined to expend time and energy debating the relative merits of value investing or fundamental analyses. Other than that, fire away!</p>
    <p class="legal">This website is published by Tall Beacons Ltd. Registered in England No. 07340918. Registered office: 48 Calder Mews London N9 4QT. This website and its content is the copyright of Tall Beacons Ltd - © Tall Beacons Ltd 2011. All rights reserved. Any redistribution or reproduction of part or all of the contents in any form is prohibited other than the following: you may print or download to a local hard disk extracts for your personal and non-commercial use only you may copy the content to individual third parties for their personal use, but only if you acknowledge the website as the source of the material. You may not, except with our express written permission, distribute or commercially exploit the content. Nor may you transmit it or store it in any other website or other form of electronic retrieval system.</p>
  </footer>
</body>
</html>
```